FjellTrims Website & website development in Wordpress

Simple website for a 5 pages with some 15 products for sale.
We will sell T shirts and other Viking mens grooming products.

*****Lady barbers****
Also the company that gets awarded this job needs to be able to give me a quote to build the site in wordpress, just a design will not work.

Target Market(s)

The adventurous person likes to travels and get a good haircut

Coding

Coded - Design and coding required

Number of Pages Required

5+ page

Font styles to use
Sans Serif

Colors
3176b5
33a6d7

Requirements
Must have
• Must have a product order page for T-Shirts
Must have a travel adventure page with up to 5 recommended adventures
Must have a link to our instagram @fjelltrimsformen page that would allow a client to book a haircut
Should show female stylists cutting mens hair- So far the only pictures in the designs submitted are male barbers
Nice to have
• We have this set up in NetMarlo would like to use wordpress. Thanks!

```html
<!DOCTYPE html>
<html lang="en">
<head>
<meta charset="utf-8">
<title>FjellTrims – Haircuts for Men</title>
<link href="https://fonts.googleapis.com/css2?family=Bebas+Neue&family=Montserrat:wght@400;500;600&display=swap" rel="stylesheet">
<style>
:root{
  --blue:#3176b5;
  --sky:#33a6d7;
  --red:#d8232a;
  --ink:#1c1c1c;
  --text:#333;
  --band:#dcedf6;
  --line:#e6e6e6;
}
*{box-sizing:border-box;margin:0;padding:0}
html,body{width:1200px;height:5245px;overflow:hidden}
body{position:relative;background:#fff;font-family:"Montserrat",sans-serif;color:var(--text)}
.abs{position:absolute}
.display{font-family:"Bebas Neue",sans-serif;letter-spacing:1px;color:var(--ink);font-weight:400}
.section-title{position:absolute;left:0;width:1200px;text-align:center;font-size:56px;line-height:1}
.rule{position:absolute;left:585px;width:30px;height:3px;background:var(--blue)}
.btn{position:absolute;display:flex;align-items:center;justify-content:center;font-family:"Bebas Neue",sans-serif;font-size:16px;letter-spacing:1px;color:#fff;background:var(--blue)}
.btn.red{background:var(--red)}
.center-text{position:absolute;left:0;width:1200px;text-align:center;font-size:15px;line-height:29px;color:var(--text)}
.photo{position:absolute}

/* hero */
.hero{left:0;top:0;width:1200px;height:473px;
  background:
    radial-gradient(ellipse 420px 380px at 120px 200px,rgba(122,98,74,.95),rgba(122,98,74,0) 70%),
    radial-gradient(ellipse 260px 300px at 300px 330px,rgba(90,76,62,.8),rgba(90,76,62,0) 70%),
    radial-gradient(ellipse 220px 240px at 1010px 430px,rgba(70,62,58,.7),rgba(70,62,58,0) 70%),
    radial-gradient(ellipse 500px 260px at 760px 120px,rgba(112,134,160,.9),rgba(112,134,160,0) 75%),
    linear-gradient(180deg,#3e4f66 0%,#4b607c 55%,#3a4556 100%)}
.hero-shade{left:0;top:0;width:1200px;height:473px;background:linear-gradient(180deg,rgba(0,0,0,.15),rgba(0,0,0,0) 40%,rgba(0,0,0,.25))}
.menu-icon{left:1004px;top:51px;width:35px;height:31px}
.brand{left:0;top:160px;width:1200px;text-align:center;font-family:"Bebas Neue",sans-serif;font-size:140px;line-height:1;color:var(--blue)}
.brand-tag{left:0;top:312px;width:1200px;text-align:center;font-family:"Bebas Neue",sans-serif;font-size:30px;letter-spacing:4px;color:#fff}

/* about */
.about-title{top:552px;font-size:58px}
.about-sub{position:absolute;left:0;top:601px;width:1200px;text-align:center;font-family:"Bebas Neue",sans-serif;font-size:26px;letter-spacing:1px;color:var(--blue)}
.about-lead{position:absolute;left:0;top:676px;width:1200px;text-align:center;font-size:13px;line-height:22px;color:var(--red)}
.about-body{top:728px;font-size:13.5px;line-height:26px}

.feature-text{position:absolute;width:330px}
.feature-text h3{font-family:"Bebas Neue",sans-serif;font-size:18px;letter-spacing:1px;color:var(--ink);font-weight:400;margin:0 0 8px}
.feature-text p{font-size:13px;line-height:27px;color:var(--text)}

/* appointment */
.appt{left:0;top:1520px;width:1200px;height:366px;background:var(--band)}
.field{position:absolute;top:1768px;height:39px;background:#fff;display:flex;align-items:center;padding-left:16px;font-size:12px;color:#999;gap:10px}
.field svg{width:16px;height:16px}

/* services */
.card{position:absolute;top:2155px;height:320px;background:#fff;border:1px solid var(--line);text-align:center}
.card.active{background:radial-gradient(ellipse 120px 140px at 60% 45%,rgba(120,92,72,.55),rgba(120,92,72,0) 75%),linear-gradient(180deg,#2a2b2e,#17191c);border-color:#1e2226}
.card .ico{position:absolute;left:50%;top:50px;transform:translateX(-50%);width:62px;height:62px}
.card h4{position:absolute;left:0;width:100%;top:146px;font-family:"Bebas Neue",sans-serif;font-size:19px;letter-spacing:1px;color:var(--ink);font-weight:400}
.card p{position:absolute;left:20px;right:20px;top:178px;font-size:13px;line-height:21px;color:var(--text)}
.card .more{position:absolute;left:0;width:100%;top:243px;font-family:"Bebas Neue",sans-serif;font-size:16px;letter-spacing:1px;color:var(--ink)}
.card.active h4,.card.active p,.card.active .more{color:#fff}
.arrow{position:absolute;width:35px;height:33px;border:1px solid #a9c7e2;background:#fff;display:flex;align-items:center;justify-content:center}
.arrow svg{width:12px;height:12px}

/* reviews */
.reviews{left:0;top:2556px;width:1200px;height:524px;background:var(--band)}
.quote-mark{left:160px;top:2727px;font-family:Georgia,serif;font-size:110px;line-height:1;color:#c9dfee}
.quote{left:175px;top:2780px;width:370px;font-size:14px;line-height:28.5px;color:var(--text)}
.reviewer{left:175px;top:2936px;font-family:"Bebas Neue",sans-serif;font-size:21px;letter-spacing:1px;color:var(--red)}
.review-photo{left:599px;top:2728px;width:440px;height:374px;
  background:
    radial-gradient(ellipse 160px 120px at 330px 110px,rgba(200,170,140,.55),rgba(200,170,140,0) 75%),
    radial-gradient(ellipse 180px 150px at 200px 190px,rgba(168,122,92,.85),rgba(168,122,92,0) 75%),
    radial-gradient(ellipse 170px 130px at 260px 300px,rgba(110,54,36,.9),rgba(110,54,36,0) 75%),
    linear-gradient(135deg,#3a2e27 0%,#5a4132 50%,#1e1917 100%)}

/* stylists */
.stylist{position:absolute;top:3396px;height:356px}
.stylist .shade{position:absolute;left:0;right:0;bottom:0;height:150px;background:linear-gradient(to bottom,rgba(0,0,0,0),rgba(0,0,0,.85))}
.stylist-figure{position:absolute;top:3294px;height:360px}
.stylist .name{position:absolute;left:0;width:100%;top:262px;text-align:center;font-family:"Bebas Neue",sans-serif;font-size:23px;letter-spacing:1px;color:#fff}
.stylist .role{position:absolute;left:0;width:100%;top:288px;text-align:center;font-size:12px;color:#ddd}
.stylist .social{position:absolute;left:50%;top:316px;transform:translateX(-50%);display:flex;gap:8px}
.stylist .social i{display:block;width:10px;height:10px;background:#fff;border-radius:2px}

/* products */
.product{position:absolute;top:4019px;height:277px;background:#fff;border:1px solid var(--line);text-align:center}
.product .pic{position:absolute;left:32px;right:32px;top:28px;height:160px;border-radius:6px}
.product h5{position:absolute;left:0;width:100%;top:212px;font-family:"Bebas Neue",sans-serif;font-size:19px;letter-spacing:1px;color:var(--ink);font-weight:400}
.product .price{position:absolute;left:0;width:100%;top:240px;font-size:13px;color:var(--red)}

/* map + contact */
.map{left:0;top:4459px;width:1200px;height:350px;
  background:
    radial-gradient(ellipse 260px 120px at 280px 120px,rgba(190,212,236,.9),rgba(190,212,236,0) 75%),
    radial-gradient(ellipse 300px 140px at 950px 230px,rgba(196,216,238,.9),rgba(196,216,238,0) 75%),
    radial-gradient(ellipse 200px 110px at 620px 280px,rgba(205,222,240,.9),rgba(205,222,240,0) 75%),
    linear-gradient(135deg,#e9eff8,#dbe6f3 55%,#e6edf6)}
.map-label{left:672px;top:4604px;width:140px;height:52px;background:var(--red);color:#fff;font-size:12px;line-height:17px;padding:9px 0 0 14px}
.contact{left:0;top:4809px;width:1200px;height:379px;
  background:
    radial-gradient(ellipse 300px 160px at 600px 60px,rgba(120,120,120,.35),rgba(120,120,120,0) 75%),
    radial-gradient(ellipse 200px 200px at 150px 250px,rgba(90,70,55,.45),rgba(90,70,55,0) 75%),
    radial-gradient(ellipse 220px 200px at 1050px 260px,rgba(90,70,55,.45),rgba(90,70,55,0) 75%),
    linear-gradient(180deg,#2c3035,#1b1e22)}
.invite{left:0;top:4890px;width:1200px;text-align:center;font-family:"Bebas Neue",sans-serif;font-size:22px;letter-spacing:2px;color:#fff}
.invite-phone{left:0;top:4920px;width:1200px;text-align:center;font-family:"Bebas Neue",sans-serif;font-size:32px;letter-spacing:1px;color:#fff}
.info{position:absolute;top:5017px}
.info h6{font-family:"Bebas Neue",sans-serif;font-size:22px;letter-spacing:1px;color:#fff;font-weight:400;display:flex;align-items:center;gap:8px}
.info h6 svg{width:16px;height:18px}
.info p{font-size:13.5px;line-height:22px;color:#e5e5e5;margin-left:24px}
.footer{left:0;top:5188px;width:1200px;height:57px;background:var(--blue)}
.copyright{left:163px;top:5208px;font-size:12.5px;color:#fff}
.soc{position:absolute;top:5199px;width:29px;height:29px}
</style>
</head>
<body>

<!-- HERO -->
<div class="abs hero photo" role="img" aria-label="Rock climber on a sunlit cliff face above the sea"></div>
<div class="abs hero-shade"></div>
<div class="btn red" style="left:161px;top:45px;width:167px;height:41px;font-size:15px">Make an appointment</div>
<svg class="abs menu-icon" viewBox="0 0 35 31"><rect x="0" y="0" width="35" height="31" fill="#d8232a"/><g fill="#fff"><rect x="4" y="5" width="11" height="5"/><rect x="19" y="5" width="12" height="5"/><rect x="4" y="13" width="11" height="5"/><rect x="19" y="13" width="12" height="5"/><rect x="4" y="21" width="27" height="5"/></g></svg>
<div class="abs brand">FjellTrims</div>
<div class="abs brand-tag">Haircuts for Men</div>

<!-- ABOUT -->
<h1 class="display section-title about-title">About FjellTrims</h1>
<div class="about-sub">Haircuts for Men</div>
<div class="rule" style="top:640px"></div>
<p class="about-lead">Lorem ipsum dolor sit amet, consectetuer adipiscing elit, sed diam nonummy nibh euismod<br>tincidunt ut laoreet dolore magna</p>
<p class="center-text about-body">Lorem ipsum dolor sit amet, consectetuer adipiscing elit, sed diam nonummy nibh euismod tincidunt ut laoreet dolore magna<br>aliquam erat volutpat. Ut wisi enim ad minim veniam, quis nostrud exerci tation ulla mcorper suscipit lobortis nisl ut aliquip ex<br>ea com modo consequat. Duis autem vel eum iriure dolor in hendrerit in vulputate velit esse molestie consequat, vel illum<br>veniam, quis nostrud exercitation &nbsp;dolore eu feugiat nulla facilisis at</p>
<div class="btn" style="left:542px;top:853px;width:114px;height:41px">Read more</div>

<div class="photo" style="left:161px;top:974px;width:438px;height:236px;background:radial-gradient(ellipse 160px 90px at 260px 40px,#f4f6f8,rgba(244,246,248,0) 75%),radial-gradient(ellipse 180px 120px at 110px 190px,#5b636b,rgba(91,99,107,0) 75%),radial-gradient(ellipse 60px 50px at 310px 120px,rgba(150,40,40,.7),rgba(150,40,40,0) 75%),linear-gradient(160deg,#d9dee3,#a3acb4 45%,#6e777f 100%)" role="img" aria-label="Mountaineer climbing a snowy peak"></div>
<svg class="abs" style="left:654px;top:1010px;width:82px;height:76px" viewBox="0 0 82 76" fill="#3176b5"><circle cx="34" cy="8" r="7"/><path d="M26 18h14l6 20 12 8-3 5-15-9-4-8-5 14 8 12-5 4-10-14 3-20-5 6-8-3z"/><rect x="4" y="22" width="12" height="20" rx="2"/><path d="M10 74L82 36v38z"/></svg>
<div class="feature-text" style="left:654px;top:1103px"><h3>Lorem ipsum dolor sit amet</h3><p>Lorem ipsum dolor sit amet, consectetuer adip<br>iscing elit, sed diam nonummy nibh euismod</p></div>

<div class="photo" style="left:601px;top:1210px;width:438px;height:236px;background:radial-gradient(ellipse 170px 60px at 200px 180px,rgba(235,242,246,.95),rgba(235,242,246,0) 75%),radial-gradient(ellipse 50px 30px at 300px 120px,rgba(210,220,60,.8),rgba(210,220,60,0) 75%),linear-gradient(180deg,#7fa6c2 0%,#4d7fa1 40%,#2f6584 70%,#24546e 100%)" role="img" aria-label="Surfer riding a breaking wave"></div>
<svg class="abs" style="left:161px;top:1245px;width:74px;height:74px" viewBox="0 0 74 74" fill="none" stroke="#3176b5" stroke-width="6"><path d="M10 50A30 30 0 0 1 58 12"/><circle cx="46" cy="22" r="6" fill="#3176b5" stroke="none"/><path d="M30 34l14 2 6 14"/><path d="M22 62h40" stroke-width="5"/></svg>
<div class="feature-text" style="left:161px;top:1337px"><h3>Lorem ipsum dolor sit amet</h3><p>Lorem ipsum dolor sit amet, consectetuer adip<br>iscing elit, sed diam nonummy nibh euismod</p></div>

<!-- APPOINTMENT -->
<div class="abs appt"></div>
<h2 class="display section-title" style="top:1598px">Make an appointment</h2>
<div class="rule" style="top:1664px"></div>
<p class="center-text" style="top:1683px;font-size:15.5px">Lorem ipsum dolor sit amet, consectetuer adipiscing elit, sed diam nonummy nibh<br>euismod tincidunt ut laoreet dolore magna aliquam erat volutpat.</p>
<div class="field" style="left:161px;width:210px"><svg viewBox="0 0 16 16" fill="none" stroke="#d8232a" stroke-width="1.3"><circle cx="8" cy="5" r="3.5"/><path d="M2 15c0-4 3-6 6-6s6 2 6 6"/></svg>Name</div>
<div class="field" style="left:385px;width:208px"><svg viewBox="0 0 16 16" fill="none" stroke="#d8232a" stroke-width="1.3"><path d="M3 1h3l1.5 4-2 1.5a9 9 0 0 0 4 4l1.5-2 4 1.5v3c0 1-1 2-2 2C7 15 1 9 1 3c0-1 1-2 2-2z"/></svg>Phone</div>
<div class="field" style="left:607px;width:208px"><svg viewBox="0 0 16 16" fill="none" stroke="#d8232a" stroke-width="1.3"><path d="M1 8L15 1 11 15 8 9z"/><path d="M8 9l7-8"/></svg>Email</div>
<div class="btn" style="left:827px;top:1768px;width:212px;height:39px">Make an appointment</div>

<!-- SERVICES -->
<h2 class="display section-title" style="top:1970px">Our services</h2>
<div class="rule" style="top:2032px"></div>
<p class="center-text" style="top:2060px;font-size:15.5px">FjellTrims is an amazing barbershop.<br>located in the heart of 418 Harbor Lane, Suite 2 Northvale, Lakeshire</p>

<div class="arrow" style="left:104px;top:2300px"><svg viewBox="0 0 12 12" fill="none" stroke="#999" stroke-width="1.5"><path d="M8 1L3 6l5 5"/></svg></div>
<div class="arrow" style="left:1059px;top:2300px;border-color:var(--blue)"><svg viewBox="0 0 12 12" fill="none" stroke="#3176b5" stroke-width="1.8"><path d="M4 1l5 5-5 5"/></svg></div>

<div class="card" style="left:161px;width:204px">
  <svg class="ico" viewBox="0 0 62 62" fill="none" stroke="#d8232a" stroke-width="2.5"><circle cx="18" cy="48" r="8"/><circle cx="42" cy="48" r="8"/><path d="M22 41L46 6M38 41L14 6"/></svg>
  <h4>Haircutting</h4><p>Lorem ipsum dolor sit amet consectetuerad</p><div class="more">Read more</div>
</div>
<div class="card active photo" style="left:385px;width:204px" role="img" aria-label="Stylist shaving a client, dark overlay">
  <svg class="ico" viewBox="0 0 62 62" fill="none" stroke="#33a6d7" stroke-width="2.5"><path d="M14 50c10 4 26 2 34-12L40 32C34 42 24 46 14 50z"/><path d="M40 32l6-10"/><path d="M20 14l2 5 5 2-5 2-2 5-2-5-5-2 5-2z"/></svg>
  <h4>Shaving</h4><p>Lorem ipsum dolor sit amet consectetuerad</p><div class="more">Read more</div>
</div>
<div class="card" style="left:609px;width:204px">
  <svg class="ico" viewBox="0 0 62 62" fill="none" stroke="#d8232a" stroke-width="2.5"><path d="M8 54l18-18"/><rect x="24" y="10" width="18" height="34" rx="9" transform="rotate(45 33 27)"/><path d="M30 16l4 4M36 12l4 4M26 22l4 4M22 28l4 4"/></svg>
  <h4>Styling</h4><p>Lorem ipsum dolor sit amet consectetuerad</p><div class="more">Read more</div>
</div>
<div class="card" style="left:833px;width:206px">
  <svg class="ico" style="top:60px" viewBox="0 0 62 62" fill="none" stroke="#33a6d7" stroke-width="2.5"><rect x="20" y="14" width="16" height="40" rx="4" transform="rotate(35 28 34)"/><path d="M38 10l10 7"/><circle cx="26" cy="36" r="3"/></svg>
  <h4 style="top:156px">Trimming</h4><p style="top:188px">Lorem ipsum dolor sit amet consectetuerad</p><div class="more" style="top:253px">Read more</div>
</div>

<!-- REVIEWS -->
<div class="abs reviews"></div>
<h2 class="display section-title" style="top:2622px">Happy customers reviews</h2>
<div class="rule" style="top:2685px"></div>
<div class="abs quote-mark">“</div>
<p class="abs quote">I love how you treat your customers. You guys are great! Thanks you your amazing staff I have this awesome look that makes everyone jealous. It matters when you give advice and share your opinion. Thanks again, you rock.</p>
<div class="abs reviewer">Arne Dalvik</div>
<svg class="abs" style="left:176px;top:2988px;width:44px;height:18px" viewBox="0 0 44 18" fill="none" stroke-width="2"><path d="M8 2L2 9l6 7" stroke="#a9c7e2"/><path d="M30 2l6 7-6 7" stroke="#3176b5"/></svg>
<div class="abs photo review-photo" role="img" aria-label="Stylist trimming a bearded client's beard with a comb"></div>
<svg class="abs" style="left:792px;top:2889px;width:54px;height:54px" viewBox="0 0 54 54" fill="none" stroke="#d8232a" stroke-width="3"><circle cx="27" cy="27" r="24"/><path d="M22 17v20l15-10z" fill="#d8232a" stroke="none"/></svg>

<!-- STYLISTS -->
<h2 class="display section-title" style="top:3186px">Our stylist</h2>
<div class="rule" style="top:3247px"></div>

<div class="stylist photo" style="left:159px;width:273px;background:radial-gradient(ellipse 110px 150px at 50% 40%,rgba(235,225,215,.55),rgba(235,225,215,0) 75%),radial-gradient(ellipse 140px 120px at 50% 80%,rgba(25,25,28,.9),rgba(25,25,28,0) 75%),linear-gradient(135deg,#7d8894,#4a525c 55%,#2c3138)" role="img" aria-label="Female stylist with arms crossed in a black apron"><div class="shade"></div><div class="name">Ingrid Holm</div><div class="role">Haircutting</div><div class="social"><i></i><i></i><i></i></div></div>
<div class="stylist photo" style="left:462px;width:273px;background:radial-gradient(ellipse 110px 150px at 50% 38%,rgba(225,190,160,.55),rgba(225,190,160,0) 75%),radial-gradient(ellipse 140px 120px at 50% 80%,rgba(28,24,22,.9),rgba(28,24,22,0) 75%),linear-gradient(135deg,#8a7563,#5a4a3d 55%,#30281f)" role="img" aria-label="Female stylist holding scissors"><div class="shade"></div><div class="name">Sigrid Berg</div><div class="role">Haircutting</div><div class="social"><i></i><i></i><i></i></div></div>
<div class="stylist photo" style="left:766px;width:273px;background:radial-gradient(ellipse 110px 150px at 50% 38%,rgba(230,205,180,.5),rgba(230,205,180,0) 75%),radial-gradient(ellipse 140px 120px at 50% 80%,rgba(22,22,26,.9),rgba(22,22,26,0) 75%),linear-gradient(135deg,#6f7c8a,#46505c 55%,#282d34)" role="img" aria-label="Female stylist holding a round brush"><div class="shade"></div><div class="name">Astrid Lund</div><div class="role">Haircutting</div><div class="social"><i></i><i></i><i></i></div></div>
<div class="btn" style="left:548px;top:3793px;width:104px;height:39px">View all</div>

<!-- PRODUCTS -->
<h2 class="display section-title" style="top:3916px">Our products</h2>
<div class="rule" style="top:3976px"></div>
<div class="arrow" style="left:104px;top:4141px"><svg viewBox="0 0 12 12" fill="none" stroke="#999" stroke-width="1.5"><path d="M8 1L3 6l5 5"/></svg></div>
<div class="arrow" style="left:1059px;top:4141px;border-color:var(--blue)"><svg viewBox="0 0 12 12" fill="none" stroke="#3176b5" stroke-width="1.8"><path d="M4 1l5 5-5 5"/></svg></div>

<div class="product" style="left:161px;width:163px"><div class="pic" role="img" aria-label="Beard shampoo bottle and box" style="background:radial-gradient(ellipse 50px 80px at 40% 60%,#3f8ea6,rgba(63,142,166,0) 80%),radial-gradient(ellipse 40px 80px at 72% 45%,#2a3f52,rgba(42,63,82,0) 80%),#fff"></div><h5>Beard shampoo</h5><div class="price">$44.39</div></div>
<div class="product" style="left:340px;width:161px"><div class="pic" role="img" aria-label="Navy T-shirt with red print" style="background:radial-gradient(ellipse 30px 30px at 50% 45%,rgba(200,40,45,.8),rgba(200,40,45,0) 80%),radial-gradient(ellipse 60px 80px at 50% 50%,#1f2a5c,rgba(31,42,92,0) 85%),#fff"></div><h5>T shirt</h5><div class="price">$35.39</div></div>
<div class="product" style="left:517px;width:163px"><div class="pic" role="img" aria-label="Shaving brush" style="background:radial-gradient(ellipse 40px 35px at 50% 28%,#cfc8bd,rgba(207,200,189,0) 85%),radial-gradient(ellipse 25px 45px at 50% 72%,#141414,rgba(20,20,20,0) 85%),#fff"></div><h5>Shave brush</h5><div class="price">$24.39</div></div>
<div class="product" style="left:695px;width:163px"><div class="pic" role="img" aria-label="Black cap with red print" style="background:radial-gradient(ellipse 20px 18px at 50% 45%,rgba(200,40,45,.8),rgba(200,40,45,0) 80%),radial-gradient(ellipse 60px 45px at 50% 52%,#1a1a1a,rgba(26,26,26,0) 85%),#fff"></div><h5>Cap</h5><div class="price">$14.39</div></div>
<div class="product" style="left:874px;width:165px"><div class="pic" role="img" aria-label="Beard oil bottle and box" style="background:radial-gradient(ellipse 35px 70px at 38% 55%,#c9a583,rgba(201,165,131,0) 85%),radial-gradient(ellipse 22px 55px at 70% 60%,#7a3f22,rgba(122,63,34,0) 85%),#fff"></div><h5>Beard oil</h5><div class="price">$15.39</div></div>

<div class="btn" style="left:481px;top:4343px;width:114px;height:39px">View all</div>
<div class="btn red" style="left:603px;top:4343px;width:116px;height:39px">Shop now</div>

<!-- MAP -->
<div class="abs map" role="img" aria-label="Street map around the barbershop location"></div>
<div class="abs map-label">418 Harbor Lane,<br>Suite 2 Northvale</div>
<svg class="abs" style="left:594px;top:4654px;width:22px;height:30px" viewBox="0 0 22 30"><path d="M11 0C5 0 0 5 0 11c0 8 11 19 11 19s11-11 11-19C22 5 17 0 11 0z" fill="#d8232a"/><circle cx="11" cy="11" r="4" fill="#fff"/></svg>

<!-- CONTACT -->
<div class="abs contact photo" role="img" aria-label="Dim barbershop interior"></div>
<div class="abs invite">We invite you to contact us</div>
<div class="abs invite-phone">+1 555 210 4836</div>

<div class="info" style="left:196px">
  <h6><svg viewBox="0 0 16 18"><path d="M8 0C4 0 1 3 1 7c0 5 7 11 7 11s7-6 7-11c0-4-3-7-7-7z" fill="#33a6d7"/><circle cx="8" cy="7" r="2.5" fill="#1f2327"/></svg>Address</h6>
  <p>418 Harbor Lane,<br>Suite 2 Northvale, LAKESHIRE</p>
</div>
<div class="info" style="left:497px">
  <h6><svg viewBox="0 0 16 18"><path d="M3 1h3l1.5 4-2 1.5a9 9 0 0 0 4 4l1.5-2 4 1.5v3c0 1-1 2-2 2C7 15 1 9 1 3c0-1 1-2 2-2z" fill="#33a6d7"/></svg>Phone / E-mail</h6>
  <p>+1 555 210 4836<br>info@fjelltrims.com</p>
</div>
<div class="info" style="left:754px">
  <h6><svg viewBox="0 0 16 18"><path d="M1 9L15 2 11 16 8 10z" fill="#33a6d7"/></svg>Opening hours</h6>
  <p>Monday - Friday: 8:00 - 16:00<br>Saturday: 8:00 - 15:00</p>
</div>

<div class="abs footer"></div>
<div class="abs copyright">Copyright © 2021 FJELLTRIMS. All Rights Reserved.</div>
<div class="soc" style="left:905px;background:#2f5fa8"></div>
<div class="soc" style="left:940px;background:#33a6d7"></div>
<div class="soc" style="left:975px;background:#2a6fb0"></div>
<div class="soc" style="left:1010px;background:#d8232a"></div>

</body>
</html>
```